Business Card design for shipping company 'FARNHOLT MARITIME LTD'

Classic / traditional business card in black Garamond / Times New Roman or similar text for a shipping / marine transport company, containing the following information:

QUOTE

FARNHOLT MARITIME LTD

PETER CALLOWAY FICS

T: +44 7923 615087
E: vessels@farnholt-mar.com

UNQUOTE

Target Market(s)

Marine / Shipping industry

Contact Information for Business Card

FARNHOLT MARITIME LTD PETER CALLOWAY FICS T: +44 7923 615087 E: vessels@farnholt-mar.com

Font styles to use
Serif

Colors

Designer to choose colors to be used in the design.

Requirements
Must have
• Garamond / Times New Roman or similar text in black colour

```html
<!DOCTYPE html>
<html lang="en">
<head>
<meta charset="utf-8">
<title>Farnholt Maritime Ltd — Business Card</title>
<link rel="stylesheet" href="https://fonts.googleapis.com/css2?family=Tinos:wght@400;700&display=swap">
<style>
  :root {
    --backdrop: #8a8a8a;
    --card: #000000;
    --ink-light: #ffffff;
    --ink-dark: #000000;
    --icon: #9a9a9a;
    --serif: "Tinos", "Times New Roman", serif;
  }
  * { margin: 0; padding: 0; box-sizing: border-box; }
  html, body {
    width: 1199px;
    height: 1200px;
    overflow: hidden;
    background: var(--backdrop);
  }
  .sheet {
    position: relative;
    width: 1199px;
    height: 1200px;
  }
  .card {
    position: absolute;
    left: 160px;
    width: 880px;
    height: 503px;
    background: var(--card);
    overflow: hidden;
    font-family: var(--serif);
  }
  .card--front { top: 64px; }
  .card--back  { top: 633px; }

  .company-name {
    position: absolute;
    left: 118px;
    top: 218px;
    color: var(--ink-light);
    font-weight: 700;
    font-size: 31px;
    letter-spacing: 0.5px;
  }
  .rule-bottom {
    position: absolute;
    left: 26px;
    top: 453px;
  }

  .rule-side {
    position: absolute;
    left: 40px;
    width: 14px;
  }
  .rule-side--top { top: 0; }
  .rule-side--bottom { top: 368px; }

  .name-tab {
    position: absolute;
    right: 0;
    top: 140px;
    width: 392px;
    height: 56px;
    background: var(--ink-light);
    border-radius: 28px 0 0 28px;
    display: flex;
    align-items: center;
    padding-left: 22px;
    color: var(--ink-dark);
    font-weight: 700;
    font-size: 24px;
    letter-spacing: 0.3px;
  }

  .contact-list {
    position: absolute;
    left: 38px;
    top: 266px;
    list-style: none;
    color: var(--ink-light);
    font-size: 26px;
    letter-spacing: 2px;
  }
  .contact-item {
    display: flex;
    align-items: center;
    gap: 12px;
    height: 36px;
    margin-bottom: 14px;
  }
  .contact-icon {
    width: 18px;
    height: 18px;
    flex: none;
  }
</style>
</head>
<body>
<main class="sheet">

  <section class="card card--front" aria-label="Card front">
    <p class="company-name">FARNHOLT MARITIME LTD</p>
    <svg class="rule-bottom" width="828" height="14" viewBox="0 0 828 14" aria-hidden="true">
      <path d="M6 7 C120 4 300 9 420 6 C560 4 700 8 822 6" stroke="var(--ink-light)" stroke-width="8" stroke-linecap="round" fill="none"/>
    </svg>
  </section>

  <section class="card card--back" aria-label="Card back">
    <svg class="rule-side rule-side--top" height="210" viewBox="0 0 14 210" aria-hidden="true">
      <path d="M7 0 L7 203" stroke="var(--ink-light)" stroke-width="10" stroke-linecap="round" fill="none"/>
    </svg>
    <svg class="rule-side rule-side--bottom" height="135" viewBox="0 0 14 135" aria-hidden="true">
      <path d="M7 7 L7 135" stroke="var(--ink-light)" stroke-width="10" stroke-linecap="round" fill="none"/>
    </svg>

    <div class="name-tab">PETER CALLOWAY FICS</div>

    <ul class="contact-list">
      <li class="contact-item">
        <svg class="contact-icon" viewBox="0 0 18 18" aria-hidden="true">
          <circle cx="9" cy="9" r="9" fill="var(--icon)"/>
          <path d="M6 5 L8 5 L8.6 7.4 L7.6 8.2 C8.2 9.6 9 10.4 10.2 11 L11 10 L13 10.8 L13 12.8 C9 13.4 5 9.6 6 5 Z" fill="var(--card)"/>
        </svg>
        <span>+44 7923 615087</span>
      </li>
      <li class="contact-item">
        <svg class="contact-icon" viewBox="0 0 18 18" aria-hidden="true">
          <circle cx="9" cy="9" r="9" fill="var(--icon)"/>
          <rect x="4.5" y="6" width="9" height="6.5" fill="none" stroke="var(--card)" stroke-width="1.2"/>
          <path d="M4.5 6 L9 9.6 L13.5 6" fill="none" stroke="var(--card)" stroke-width="1.2"/>
        </svg>
        <span>vessels@farnholt-mar.com</span>
      </li>
    </ul>
  </section>

</main>
</body>
</html>
```